LHW TMA Website

Would like to have a website created that keeps with the branding of our other company; Larkfield Harbor Corporation. www.larkfieldharbor.net

Target Market(s)

Medical providers, accounts receivable management

Industry/Entity Type

Accounts Receivable Management

Number of Pages Required

5+ page

Requirements
Must have
• look similar to www.larkfieldharbor.net, but will have different logo and domain as it is completely separate company

```html
<!DOCTYPE html>
<html lang="en">
<head>
<meta charset="utf-8">
<title>LHW TMA</title>
<link rel="stylesheet" href="https://fonts.googleapis.com/css2?family=Poppins:wght@700;800&family=PT+Sans:ital,wght@0,400;0,700;1,400&display=swap">
<style>
:root{
  --green-dark:#2b4f49;
  --green:#5e9e8a;
  --green-soft:#6aa592;
  --wine:#6c3336;
  --teal-deep:#2c5650;
  --ink:#333;
  --grey:#666;
  --footer:#3a3a3a;
  --white:#fff;
  --star:#c6b23a;
}
*{margin:0;padding:0;box-sizing:border-box}
html,body{width:1200px;height:3053px;overflow:hidden;background:var(--white)}
body{position:relative;font-family:"PT Sans",sans-serif;color:var(--ink)}
.abs{position:absolute}
.top-rule{left:0;top:0;width:1200px;height:3px;background:var(--green)}
.logo{left:142px;top:22px;font-family:"Poppins",sans-serif;font-weight:800;font-size:36px;color:var(--green-dark);letter-spacing:.5px}
.nav{top:34px;font-size:15px;font-weight:700;color:var(--ink)}
.nav.active{border-bottom:3px solid var(--green);padding-bottom:4px}
.btn{display:flex;align-items:center;justify-content:center;background:var(--green-dark);color:var(--white);border-radius:40px;font-weight:700}
.login{left:904px;top:19px;width:150px;height:47px;font-size:15px}
.hero{left:0;top:86px;width:1200px;height:474px;background:linear-gradient(90deg,#6f7676 0%,#8b9293 40%,#b7b2ab 60%,#3f5a58 100%)}
.hero-title{left:142px;top:174px;font-family:"Poppins",sans-serif;font-weight:800;font-size:57px;line-height:62px;color:var(--white)}
.hero-btn{left:142px;top:400px;width:215px;height:66px;font-size:21px}
.dot{left:1113px;width:8px;height:8px;border-radius:50%;background:var(--white)}
.tile{top:560px;height:244px;display:flex;flex-direction:column;align-items:center;color:var(--white);font-size:21px;font-weight:700;text-align:center;line-height:29px}
.tile .icon{width:92px;height:92px;margin:30px 0 28px;border-radius:50%;background:rgba(255,255,255,.25)}
.welcome{left:0;top:902px;width:1200px;text-align:center;font-family:"Poppins",sans-serif;font-weight:800;font-size:45px;color:var(--green-dark)}
.intro{left:210px;top:990px;width:780px;text-align:center;font-size:17px;line-height:29px;color:var(--grey)}
.list{top:1152px;list-style:none;font-size:16.5px;font-weight:700;line-height:28.7px;color:var(--ink)}
.list li{display:flex;align-items:center;gap:14px}
.list svg{width:17px;height:17px;flex:none}
.read{left:492px;top:1360px;width:215px;height:65px;font-size:21px}
.band{left:0;top:1690px;width:1200px;height:496px;background:var(--green-soft)}
.photo{left:216px;top:1503px;width:767px;height:366px;background:linear-gradient(135deg,#c9cfcb,#7f8d8f 55%,#3f4a55)}
.save-title{left:0;top:1908px;width:1200px;text-align:center;font-family:"Poppins",sans-serif;font-weight:800;font-size:45px;color:var(--white)}
.save-sub{left:0;top:1990px;width:1200px;text-align:center;font-size:16px;font-weight:700;color:var(--white)}
.save-btn{left:492px;top:2046px;width:215px;height:65px;font-size:21px}
.avatar{left:538px;top:2261px;width:124px;height:124px;border-radius:50%;background:linear-gradient(#8f8f8f,#c7b59a)}
.name{left:0;top:2408px;width:1200px;text-align:center;font-size:21px;font-weight:700;color:var(--green-dark)}
.name em{font-weight:400;font-size:16px;color:var(--ink)}
.stars{left:0;top:2447px;width:1200px;text-align:center;color:var(--star);font-size:13px;letter-spacing:1px}
.quote{left:190px;top:2497px;width:820px;text-align:center;font-style:italic;font-size:16.5px;line-height:29px;color:var(--ink)}
.arrow{top:2649px;width:44px;height:44px;border:1.5px solid var(--ink);border-radius:50%}
.footer{left:0;top:2748px;width:1200px;height:305px;background:var(--footer);color:var(--white)}
.f-head{top:2812px;font-size:21px;font-weight:700;color:var(--white)}
.f-links{left:153px;top:2866px;list-style:none;font-size:14px;line-height:28.8px;color:var(--white)}
.f-contact{left:320px;font-size:14px;line-height:23px;color:var(--white);display:flex;gap:10px}
.f-contact svg{width:15px;height:15px;flex:none;margin-top:4px}
.social{top:2871px;width:28px;height:28px;border-radius:50%;background:var(--white)}
.badge{left:880px;top:2817px;width:166px;height:62px;border-radius:6px;background:#1d4e86;border:2px solid var(--white)}
.copy{left:662px;top:2965px;font-size:13px;color:var(--white)}
.chat{left:1140px;top:2799px;width:54px;height:174px;border-radius:27px;background:var(--green-dark);display:flex;align-items:center;justify-content:center}
.chat span{transform:rotate(-90deg);white-space:nowrap;font-size:21px;font-weight:700;color:var(--white)}
</style>
</head>
<body>
<div class="abs top-rule"></div>
<div class="abs logo">LHW TMA</div>
<div class="abs nav active" style="left:428px">HOME</div>
<div class="abs nav" style="left:506px">ABOUT US</div>
<div class="abs nav" style="left:610px">SERVICES</div>
<div class="abs nav" style="left:709px">NEWS</div>
<div class="abs nav" style="left:786px">CONTACT US</div>
<div class="abs btn login">CLIENT LOGIN</div>

<div class="abs hero" role="img" aria-label="Smiling businesswoman in an office meeting"></div>
<div class="abs hero-title">EXPERIENCE<br>AND PROVEN<br>RESULTS</div>
<div class="abs btn hero-btn">GET STARTED</div>
<div class="abs dot" style="top:288px"></div>
<div class="abs dot" style="top:310px;background:var(--green)"></div>
<div class="abs dot" style="top:331px"></div>
<div class="abs dot" style="top:352px"></div>

<div class="abs tile" style="left:0;width:388px;background:var(--green)"><div class="icon" role="img" aria-label="Hands holding a heart icon"></div>HEALTHCARE AR<br>MANAGEMENT</div>
<div class="abs tile" style="left:388px;width:391px;background:var(--wine)"><div class="icon" role="img" aria-label="Finance chart icon"></div>COMMERCIAL AR<br>MANAGEMENT</div>
<div class="abs tile" style="left:779px;width:421px;background:var(--teal-deep)"><div class="icon" role="img" aria-label="Insurance document icon"></div>INSURANCE OVERPAYMENT<br>RECOVERY</div>

<h1 class="abs welcome">WELCOME TO LHW TMA</h1>
<p class="abs intro">Lorem ipsum dolor sit amet, consectetur adipiscing elit, sed do eiusmod tempor incididunt ut labore et dolore magna is ipsum suspendisse ultices graisus commodo viverra maecenas accumsan lacus vel facilisis. Lorem ipsum dolor sit amet, consectetur adipiscing elit, sed do eiusmod tempor incididunt ut labore et dolore magna is ipsum suspendisse ultices graisus commodo viverra maecenas accumsan lacus vel facilisis.</p>

<svg width="0" height="0" style="position:absolute"><symbol id="tick" viewBox="0 0 20 20"><circle cx="10" cy="10" r="10" fill="#5e9e8a"/><path d="M5.5 10.3l3 3 6-6.3" fill="none" stroke="#fff" stroke-width="2.2"/></symbol></svg>
<ul class="abs list" style="left:187px">
  <li><svg><use href="#tick"/></svg>AR Receivables Management-Primary and Secondary</li>
  <li><svg><use href="#tick"/></svg>Early Out-Pre Business Debt Collections</li>
  <li><svg><use href="#tick"/></svg>IVR and Online Payment Processing</li>
  <li><svg><use href="#tick"/></svg>Third Party Billing Solutions</li>
  <li><svg><use href="#tick"/></svg>Self-Pay AR Management</li>
</ul>
<ul class="abs list" style="left:666px">
  <li><svg><use href="#tick"/></svg>Bad Business Debt Collection</li>
  <li><svg><use href="#tick"/></svg>Occupational Medicine AR Management</li>
  <li><svg><use href="#tick"/></svg>Urgent Care Specialist AR Management</li>
  <li><svg><use href="#tick"/></svg>Call Center</li>
  <li><svg><use href="#tick"/></svg>Specialist Financial Counselors-CPAR certified</li>
</ul>
<div class="abs btn read">READ MORE</div>

<div class="abs band" role="img" aria-label="Green-tinted photo of business paperwork on a desk"></div>
<div class="abs photo" role="img" aria-label="Three business colleagues talking in a bright office"></div>
<h2 class="abs save-title">START SAVING NOW</h2>
<p class="abs save-sub">Reduce overhead and improve operational efficiency</p>
<div class="abs btn save-btn">GET STARTED</div>

<div class="abs avatar" role="img" aria-label="Customer portrait"></div>
<div class="abs name">- John Doe,<em>Customer</em></div>
<div class="abs stars">★★★★★</div>
<p class="abs quote">“Lorem ipsum dolor sit amet, consectetur adipiscing elit, sed do eiusmod tempor incididunt ut labore et dolore magna aliqua. Quis ipsum suspendisse ultrices gravida. Risus commodo viverra maecenas accumsan lacus vel facilisisorem ipsum dolor sit amet, consectetur adipiscing elit, sed do eiusmod tempor incididunt ut labore et dolore magna aliqua.is ipsum suspendisse ultrices gravida. Risus commodo viverra maecenas accumsan lacus vel facilisis”</p>
<svg class="abs arrow" style="left:553px" viewBox="0 0 44 44"><path d="M25 14l-8 8 8 8" fill="none" stroke="#333" stroke-width="2"/></svg>
<svg class="abs arrow" style="left:603px" viewBox="0 0 44 44"><path d="M19 14l8 8-8 8" fill="none" stroke="#333" stroke-width="2"/></svg>

<footer class="abs footer"></footer>
<div class="abs f-head" style="left:152px">LINKS</div>
<div class="abs f-head" style="left:319px">CONTACT INFO</div>
<div class="abs f-head" style="left:662px">FOLLOW US</div>
<ul class="abs f-links"><li>Home</li><li>About Us</li><li>Services</li><li>News</li><li>Contact Us</li></ul>
<div class="abs f-contact" style="top:2864px"><svg viewBox="0 0 16 16"><path d="M8 1a5 5 0 0 0-5 5c0 4 5 9 5 9s5-5 5-9a5 5 0 0 0-5-5zm0 7a2 2 0 1 1 0-4 2 2 0 0 1 0 4z" fill="#fff"/></svg><span>123,Sed ut perspiciatis unde omnis<br>iste natuatem accusantium</span></div>
<div class="abs f-contact" style="top:2924px"><svg viewBox="0 0 16 16"><path d="M3 1l3 3-2 2c1 2 3 4 5 5l2-2 3 3-2 3C6 15 1 10 1 3z" fill="#fff"/></svg><span>Phone : 1 888 888 8888</span></div>
<div class="abs f-contact" style="top:2962px"><svg viewBox="0 0 16 16"><rect x="1" y="3" width="14" height="10" fill="#fff"/><path d="M1 3l7 6 7-6" fill="none" stroke="#3a3a3a" stroke-width="1.3"/></svg><span>info@lhwtma.com</span></div>
<div class="abs social" style="left:656px"></div>
<div class="abs social" style="left:705px"></div>
<div class="abs social" style="left:757px"></div>
<div class="abs badge" role="img" aria-label="Business accreditation badge"></div>
<div class="abs copy">© 2021 LHW TMA.All Rights Reserved &nbsp;|&nbsp; Privacy Policy &nbsp;| Terms and Use</div>
<div class="abs chat"><span>LIVE CHAT</span></div>
</body>
</html>
```